2026 Compostable Stand up Pouch Redesign

Project Overview
We are a natural dog bakery focused on simple, healthy ingredients and earth-friendly packaging. As the first step in a rebrand, we are redesigning our 6 oz stand-up pouch using new compostable packaging materials.
New pouch is the same size and structure as current (template provided)
Files included:
Existing Art template (PDF + JPG)
Photos of current packaging (for reference only)
Copy of existing logo (Meadowlark Treat Kitchen)
Copy of future logo (Birchwood Natural Bakery)
This redesign should feel like a clear upgrade—more refined, more intentional, and more aligned with sustainability.
⚠️ IMPORTANT LAYOUT CONSTRAINT (PLEASE READ)
The new pouch has a full-width horizontal window.
Design elements may ONLY appear above and below the window
No design elements can be placed to the left or right of the window
A 4.5" W x 3.5" H blank space above the window must be preserved
This is reserved for applied product labels
Keep this area completely clean (no textures, patterns, or graphics)
Submissions that ignore these elements will not be considered.
Brand Direction & Style
We are looking for a design that feels:
Natural and ingredient-focused
Eco-conscious and sustainable
Clean and elevated (not rustic, not overly playful)
Warm and trustworthy
Avoid:
Neon or bright artificial colors
Loud, busy, or overly commercial designs
Cartoon-heavy or overly whimsical styles
Color Direction
Our current packaging is kraft brown, but the new material allows full-color printing. We are looking for:
Nature-inspired colors only
Greens, muted blues, warm browns, soft earth tones
Background color is flexible within this palette
Must work with:
Current logo: Meadowlark Treat Kitchen
Future logo: Birchwood Natural Bakery
👉 For this project, use Meadowlark Treat Kitchen logo only
Front of Pouch Requirements
Do NOT include logo on pouch front
(Logo will be on applied labels)
Required Elements
Tagline: Simple, Healthy Ingredients. Earth Friendly Packaging.
Compostable Messaging (REQUIRED):
Must clearly communicate that packaging is compostable
Optional placement:
Tear-off strip near hang hole
BUT must also appear somewhere on the main pouch design
Origin Callout:
“Hand Made in the Pacific Northwest”
Can be a badge, stamp, or graphic (open to redesign)
Icons (Highly Encouraged)
We would like to explore a clean, minimal icon set for:
No Corn
No Wheat
No Soy
No GMOs
Compostable Packaging
(Keep icons simple, clean, and consistent with natural aesthetic)
Back of Pouch Requirements
Messaging Direction
Do NOT use: “The healthiest pet bakery in the US”
Instead, build around:
Simple, Healthy Ingredients. Earth Friendly Packaging.
Content
“Our Recipes” bullet points (from current packaging – still valid)
Sustainability messaging:
Include reference to reducing our “carbon pawprint”
Emphasize eco-friendly materials and practices
Design Direction
Open to new layout and graphics
Should visually reinforce:
Clean ingredients
Natural sourcing
Sustainability
Printing Considerations
Design should be mindful of production scalability:
Should translate well to both digital and roto printing
Avoid overly complex gradients or excessive color layering
Creative Freedom (Important)
While we have outlined structure and constraints, we are intentionally leaving visual interpretation open.
We welcome:
Fresh layout ideas
Refined graphic elements
Elevated visual storytelling
We are especially interested in designs that feel:
Thoughtful
Clean
Naturally premium
Any design submission that includes loud, neon, or "aggressive" color schemes or a mass market appeal will be eliminated immediately. We are a premium, natural dog bakery found in independent stores only.
UPDATED & IMPORTANT DESIGN REQUIREMENTS (PLEASE READ)
This pouch is a base design used across all flavors. A separate product label will be applied.
A clearly defined blank area must be left for label placement (do not incorporate into artwork).
The product viewing window is fixed:
Size and placement must match the template exactly
Do not resize, reposition, or redesign the window
Designs that do not follow these requirements will not be considered.
Please review the discussion board for additional feedback and direction before submitting revisions.

```html
<!DOCTYPE html>
<html lang="en">
<head>
<meta charset="utf-8">
<title>Meadowlark Treat Kitchen – Compostable Stand-up Pouch Dieline</title>
<link href="https://fonts.googleapis.com/css2?family=Rokkitt:wght@500;700&family=Montserrat:wght@500;600;700&display=swap" rel="stylesheet">
<style>
  :root{
    --cream:#f5f2ec;
    --forest:#1d4526;
    --lime:#b5c455;
    --bark:#5c3a1c;
    --bark-line:#6e4a2a;
    --window:#8f8f8f;
    --guide:#29abe2;
    --guide-strong:#0a6eb4;
    --trim:#f08a8a;
    --hatch:#bfe3f5;
  }
  html,body{margin:0;padding:0;width:1200px;height:2649px;overflow:hidden;background:#fff}
  .dieline{display:block;width:1200px;height:2649px}
  .serif{font-family:'Rokkitt',serif}
  .sans{font-family:'Montserrat',sans-serif}
  .dim{font-family:'Montserrat',sans-serif;font-size:10px;fill:var(--guide)}
  .dim-label{font-family:'Montserrat',sans-serif;font-weight:700;font-size:20px;fill:var(--guide-strong)}
  .guide-line{stroke:var(--guide);stroke-width:1;fill:none}
  .dash{stroke:var(--guide);stroke-width:.8;stroke-dasharray:5 4;fill:none;opacity:.7}
  .tagline{font-family:'Rokkitt',serif;font-weight:500;font-size:17px;fill:#fff}
  .icon-label{font-family:'Montserrat',sans-serif;font-size:4.5px;font-weight:600;fill:#fff}
  .back-copy{font-family:'Montserrat',sans-serif;font-size:6.5px;font-weight:600;fill:#fff}
  .box-head{font-family:'Rokkitt',serif;font-weight:700;font-size:30px;fill:#fff}
  .box-item{font-family:'Montserrat',sans-serif;font-weight:600;font-size:10px;fill:var(--forest)}
  .box-para{font-family:'Montserrat',sans-serif;font-weight:600;font-size:6.6px;fill:var(--forest)}
  .brand-name{font-family:'Rokkitt',serif;font-weight:700;font-size:26px;fill:var(--bark)}
</style>
</head>
<body>
<svg class="dieline" viewBox="0 0 909 2006" preserveAspectRatio="none" xmlns="http://www.w3.org/2000/svg">
  <defs>
    <pattern id="seal-hatch" width="8" height="8" patternUnits="userSpaceOnUse" patternTransform="rotate(45)">
      <line x1="0" y1="0" x2="0" y2="8" stroke="var(--hatch)" stroke-width="2"/>
    </pattern>
    <pattern id="bark-hatch" width="10" height="10" patternUnits="userSpaceOnUse" patternTransform="rotate(45)">
      <line x1="0" y1="0" x2="0" y2="10" stroke="var(--bark-line)" stroke-width="1.2"/>
    </pattern>
    <clipPath id="front-arc"><ellipse cx="460" cy="690" rx="300" ry="140"/></clipPath>
    <clipPath id="back-arc"><ellipse cx="460" cy="1300" rx="300" ry="135"/></clipPath>
  </defs>

  <!-- trim / bleed -->
  <rect x="194" y="67" width="532" height="1859" fill="var(--cream)" stroke="var(--trim)" stroke-width="1"/>

  <!-- ========== FRONT PANEL ========== -->
  <g class="front-panel">
    <!-- compostable tear tab -->
    <rect x="590" y="67" width="61" height="55" fill="var(--lime)"/>
    <circle cx="620" cy="126" r="30" fill="var(--forest)" stroke="var(--lime)" stroke-width="3"/>
    <text x="620" y="124" text-anchor="middle" class="serif" font-size="18" font-weight="700" fill="#fff">100%</text>
    <text x="620" y="135" text-anchor="middle" class="sans" font-size="5.5" font-weight="700" fill="#fff">COMPOSTABLE</text>
    <text x="620" y="142" text-anchor="middle" class="sans" font-size="5.5" font-weight="700" fill="#fff">PACKAGING</text>

    <!-- zipper & tear guides -->
    <line class="dash" x1="211" y1="148" x2="709" y2="148"/>
    <line class="dash" x1="211" y1="155" x2="709" y2="155"/>
    <rect x="211" y="180" width="498" height="4" fill="var(--guide-strong)"/>
    <line class="dash" x1="211" y1="198" x2="709" y2="198"/>

    <!-- tagline block -->
    <path d="M195 216 H493 a6 6 0 0 1 6 6 V269 a6 6 0 0 1 -6 6 H195 Z" fill="var(--forest)"/>
    <g stroke="#fff" stroke-width="1.5" fill="none">
      <circle cx="279" cy="234" r="5"/><path d="M276.5 234 l2 2 l4 -4"/>
      <circle cx="279" cy="258" r="5"/><path d="M276.5 258 l2 2 l4 -4"/>
    </g>
    <text x="293" y="239" class="tagline">Simple, Healthy Ingredients.</text>
    <text x="293" y="264" class="tagline">Earth Friendly Packaging.</text>

    <!-- origin badge -->
    <g class="origin-badge">
      <path d="M603 268 l8 22 l9 -8 l9 8 l8 -22 Z" fill="#f2b705"/>
      <circle cx="620" cy="245" r="31" fill="var(--forest)" stroke="var(--lime)" stroke-width="3"/>
      <circle cx="620" cy="245" r="15" fill="var(--lime)" role="img" aria-label="Outline of Washington state"/>
      <text x="620" y="225" text-anchor="middle" class="sans" font-size="5" font-weight="700" fill="#fff">HAND MADE</text>
      <text x="620" y="270" text-anchor="middle" class="sans" font-size="4.5" font-weight="700" fill="#fff">IN THE PACIFIC NW</text>
    </g>

    <!-- brown band with window cutout -->
    <path d="M194 645 H297 a7 7 0 0 1 7 7 V690 a8 8 0 0 0 8 8 H606 a8 8 0 0 0 8 -8 V652 a7 7 0 0 1 7 -7 H726 V846 H194 Z" fill="var(--bark)"/>
    <rect x="194" y="645" width="532" height="201" fill="url(#bark-hatch)" opacity=".6" clip-path="url(#front-arc)" style="display:none"/>
    <path d="M194 700 V846 H726 V700 Q700 826 460 826 Q220 826 194 700 Z" fill="url(#bark-hatch)" opacity=".7"/>
    <path d="M230 700 Q250 826 460 826 Q670 826 690 700" fill="none" stroke="var(--bark-line)" stroke-width="1"/>

    <!-- product window -->
    <rect x="310" y="591" width="299" height="106" rx="6" fill="var(--window)"/>

    <!-- free-from icon row -->
    <g class="icon-row" fill="none" stroke="var(--lime)" stroke-width="2">
      <circle cx="341" cy="740" r="25"/><circle cx="400" cy="740" r="25"/><circle cx="459" cy="740" r="25"/><circle cx="518" cy="740" r="25"/><circle cx="578" cy="740" r="25"/>
      <!-- corn -->
      <ellipse cx="341" cy="740" rx="7" ry="14"/><path d="M334 744 q-6 6 -1 14 M348 744 q6 6 1 14"/>
      <!-- wheat -->
      <path d="M400 724 v34 M400 732 l-6 -5 M400 732 l6 -5 M400 740 l-6 -5 M400 740 l6 -5 M400 748 l-6 -5 M400 748 l6 -5"/>
      <!-- soy -->
      <path d="M447 752 q4 -20 24 -24 q-4 20 -24 24 Z"/><circle cx="455" cy="744" r="2.5"/><circle cx="462" cy="737" r="2.5"/>
      <!-- dna -->
      <path d="M512 722 q12 9 0 18 q-12 9 0 18 M524 722 q-12 9 0 18 q12 9 0 18 M513 730 h10 M513 750 h10"/>
      <!-- compost leaf -->
      <path d="M570 750 q0 -20 18 -20 q0 20 -18 20 Z M570 750 l12 -12"/>
      <path d="M562 730 a18 18 0 0 1 26 -6 M594 750 a18 18 0 0 1 -26 6"/>
      <!-- slashes -->
      <path d="M323 722 l36 36 M382 722 l36 36 M441 722 l36 36 M500 722 l36 36"/>
    </g>
    <g text-anchor="middle">
      <text x="341" y="781" class="icon-label">NO CORN</text>
      <text x="400" y="781" class="icon-label">NO WHEAT</text>
      <text x="459" y="781" class="icon-label">NO SOY</text>
      <text x="518" y="781" class="icon-label">NO GMOS</text>
      <text x="578" y="779" class="icon-label">COMPOSTABLE</text>
      <text x="578" y="785" class="icon-label">PACKAGING</text>
    </g>
  </g>

  <!-- ========== GUSSET ========== -->
  <g class="gusset">
    <rect x="211" y="847" width="498" height="298" rx="12" fill="url(#seal-hatch)" stroke="var(--guide)" stroke-width="1"/>
    <ellipse cx="460" cy="1000" rx="236" ry="127" fill="#fff"/>
    <line class="dash" x1="203" y1="996" x2="718" y2="996"/>
  </g>

  <!-- ========== BACK PANEL (printed upside down) ========== -->
  <g class="back-panel">
    <rect x="194" y="1145" width="532" height="203" fill="var(--bark)"/>
    <path d="M194 1145 H726 V1290 Q700 1165 460 1165 Q220 1165 194 1290 Z" fill="url(#bark-hatch)" opacity=".7"/>
    <path d="M230 1290 Q250 1165 460 1165 Q670 1165 690 1290" fill="none" stroke="var(--bark-line)" stroke-width="1"/>

    <g text-anchor="middle">
      <text x="460" y="1298" class="back-copy" transform="rotate(180 460 1296)">OUR FOCUS IS ON REDUCING OUR CARBON PAWPRINT. THIS PACKAGE IS MADE FROM</text>
      <text x="460" y="1288" class="back-copy" transform="rotate(180 460 1286)">MATERIALS THAT ARE 100% HOME COMPOSTABLE. BY CHOOSING THIS POUCH, YOU</text>
      <text x="460" y="1278" class="back-copy" transform="rotate(180 460 1276)">ARE HELPING US PROTECT THE ENVIRONMENT ONE TREAT AT A TIME.</text>
    </g>
    <g class="contact">
      <rect x="585" y="1243" width="7" height="7" fill="var(--lime)"/>
      <text x="580" y="1250" class="back-copy" font-size="7" transform="rotate(180 580 1248)">MEADOWLARK TREAT KITCHEN</text>
      <circle cx="589" cy="1234" r="3.5" fill="var(--lime)"/>
      <text x="580" y="1237" class="back-copy" font-size="7" font-weight="500" transform="rotate(180 580 1235)">Cedar Hollow, WA</text>
      <circle cx="448" cy="1247" r="3.5" fill="var(--lime)"/>
      <text x="438" y="1250" class="back-copy" font-size="7" font-weight="500" transform="rotate(180 438 1248)">866-555-0142</text>
      <circle cx="448" cy="1234" r="3.5" fill="var(--lime)"/>
      <text x="438" y="1237" class="back-copy" font-size="7" font-weight="500" transform="rotate(180 438 1235)">meadowlarktreats.com</text>
    </g>

    <!-- eco friendly seal -->
    <circle cx="460" cy="1350" r="35" fill="var(--forest)" stroke="var(--cream)" stroke-width="3"/>
    <circle cx="460" cy="1350" r="24" fill="none" stroke="var(--lime)" stroke-width="1.5"/>
    <path d="M460 1338 q10 8 0 22 q-10 -14 0 -22 Z" fill="var(--lime)"/>
    <text x="460" y="1376" text-anchor="middle" class="sans" font-size="5.5" font-weight="700" fill="#fff" transform="rotate(180 460 1374)">ECO FRIENDLY</text>

    <!-- our recipes box -->
    <rect x="260" y="1407" width="187" height="208" rx="6" fill="var(--lime)"/>
    <path d="M260 1567 H447 V1609 a6 6 0 0 1 -6 6 H266 a6 6 0 0 1 -6 -6 Z" fill="var(--forest)"/>
    <text x="353" y="1590" text-anchor="middle" class="box-head" transform="rotate(180 353 1590)" dy="10">OUR RECIPES</text>
    <g fill="none" stroke="var(--forest)" stroke-width="1.3">
      <circle cx="425" cy="1538" r="10"/><circle cx="425" cy="1505" r="10"/><circle cx="425" cy="1474" r="10"/><circle cx="425" cy="1435" r="10"/>
    </g>
    <text x="402" y="1538" class="box-item" transform="rotate(180 402 1538)" dy="4">CLEAN &amp; SIMPLE</text>
    <text x="402" y="1505" class="box-item" transform="rotate(180 402 1505)" dy="4">NOTHING ARTIFICIAL</text>
    <text x="402" y="1480" class="box-item" transform="rotate(180 402 1480)" dy="4">HANDCRAFTED</text>
    <text x="402" y="1467" class="box-item" transform="rotate(180 402 1467)" dy="4">IN SMALL BATCHES</text>
    <text x="402" y="1441" class="box-item" transform="rotate(180 402 1441)" dy="4">PREMIUM INGREDIENTS</text>
    <text x="402" y="1428" class="box-item" transform="rotate(180 402 1428)" dy="4">FROM THE PACIFIC NW</text>

    <!-- our mission box -->
    <rect x="477" y="1407" width="186" height="208" rx="6" fill="var(--lime)"/>
    <path d="M477 1567 H663 V1609 a6 6 0 0 1 -6 6 H483 a6 6 0 0 1 -6 -6 Z" fill="var(--forest)"/>
    <text x="570" y="1590" text-anchor="middle" class="box-head" transform="rotate(180 570 1590)" dy="10">OUR MISSION</text>
    <g>
      <circle cx="630" cy="1542" r="10" fill="var(--forest)"/><path d="M625 1542 l3 4 l7 -8" stroke="var(--lime)" stroke-width="2" fill="none"/>
      <circle cx="630" cy="1500" r="10" fill="var(--forest)"/><path d="M625 1500 l3 4 l7 -8" stroke="var(--lime)" stroke-width="2" fill="none"/>
    </g>
    <text x="605" y="1549" class="box-item" transform="rotate(180 605 1549)" dy="4">SIMPLE, HEALTHY</text>
    <text x="605" y="1536" class="box-item" transform="rotate(180 605 1536)" dy="4">INGREDIENTS.</text>
    <text x="605" y="1507" class="box-item" transform="rotate(180 605 1507)" dy="4">EARTH FRIENDLY</text>
    <text x="605" y="1494" class="box-item" transform="rotate(180 605 1494)" dy="4">PACKAGING.</text>
    <text x="645" y="1468" class="box-para" transform="rotate(180 645 1468)">AT MEADOWLARK TREAT KITCHEN, WE</text>
    <text x="645" y="1459" class="box-para" transform="rotate(180 645 1459)">BELIEVE YOUR DOG DESERVES THE</text>
    <text x="645" y="1450" class="box-para" transform="rotate(180 645 1450)">BEST NATURE HAS TO OFFER. OUR</text>
    <text x="645" y="1441" class="box-para" transform="rotate(180 645 1441)">RECIPES FOCUS ON CLEAN,</text>
    <text x="645" y="1432" class="box-para" transform="rotate(180 645 1432)">NATURALLY SOURCED INGREDIENTS</text>
    <text x="645" y="1423" class="box-para" transform="rotate(180 645 1423)">TO SUPPORT A HEALTHY LIFESTYLE.</text>

    <!-- brand name -->
    <g class="brand">
      <circle cx="440" cy="1738" r="36" fill="var(--bark)"/>
      <text x="470" y="1660" text-anchor="middle" class="brand-name" transform="rotate(180 470 1660)">Meadowlark</text>
      <text x="470" y="1630" text-anchor="middle" class="brand-name" transform="rotate(180 470 1630)">Treat Kitchen</text>
    </g>

    <!-- bottom zipper & tear guides -->
    <line class="dash" x1="211" y1="1783" x2="709" y2="1783"/>
    <rect x="211" y="1798" width="498" height="4" fill="var(--guide-strong)"/>
    <line class="dash" x1="211" y1="1817" x2="709" y2="1817"/>
    <line class="dash" x1="211" y1="1843" x2="709" y2="1843"/>
  </g>

  <!-- side seals & pouch outlines -->
  <rect x="211" y="83" width="20" height="763" fill="url(#seal-hatch)"/>
  <rect x="689" y="83" width="20" height="763" fill="url(#seal-hatch)"/>
  <rect x="211" y="1145" width="20" height="765" fill="url(#seal-hatch)"/>
  <rect x="689" y="1145" width="20" height="765" fill="url(#seal-hatch)"/>
  <rect x="211" y="83" width="498" height="763" rx="12" fill="none" stroke="var(--guide-strong)" stroke-width="1"/>
  <rect x="211" y="1145" width="498" height="765" rx="12" fill="none" stroke="var(--guide-strong)" stroke-width="1"/>
  <circle cx="460" cy="115" r="13" fill="#fff" stroke="var(--guide-strong)" stroke-width="1.5"/>
  <circle cx="460" cy="1875" r="13" fill="#fff" stroke="var(--guide-strong)" stroke-width="1.5"/>
  <circle cx="214" cy="148" r="4" fill="#fff"/><circle cx="706" cy="148" r="4" fill="#fff"/>
  <circle cx="214" cy="1843" r="4" fill="#fff"/><circle cx="706" cy="1843" r="4" fill="#fff"/>

  <!-- ========== DIMENSION GUIDES ========== -->
  <g class="dimensions">
    <line class="guide-line" x1="211" y1="42" x2="709" y2="42"/>
    <line class="guide-line" x1="211" y1="34" x2="211" y2="50"/><line class="guide-line" x1="709" y1="34" x2="709" y2="50"/>
    <text x="460" y="27" text-anchor="middle" class="dim">150.00 mm (5.91 in)</text>

    <line class="guide-line" x1="117" y1="83" x2="117" y2="1910"/>
    <line class="guide-line" x1="108" y1="83" x2="126" y2="83"/><line class="guide-line" x1="108" y1="1910" x2="126" y2="1910"/>
    <text x="103" y="996" text-anchor="middle" class="dim" transform="rotate(-90 103 996)">550.00 mm (21.65 in)</text>

    <line class="guide-line" x1="161" y1="83" x2="161" y2="1910"/>
    <line class="guide-line" x1="152" y1="83" x2="170" y2="83"/><line class="guide-line" x1="152" y1="846" x2="170" y2="846"/>
    <line class="guide-line" x1="152" y1="1145" x2="170" y2="1145"/><line class="guide-line" x1="152" y1="1910" x2="170" y2="1910"/>
    <text x="148" y="465" text-anchor="middle" class="dim" transform="rotate(-90 148 465)">230.00 mm (9.06 in)</text>
    <text x="148" y="996" text-anchor="middle" class="dim" transform="rotate(-90 148 996)">90.00 mm (3.54 in)</text>
    <text x="148" y="1528" text-anchor="middle" class="dim" transform="rotate(-90 148 1528)">230.00 mm (9.06 in)</text>

    <line class="guide-line" x1="774" y1="83" x2="774" y2="148"/>
    <line class="guide-line" x1="766" y1="83" x2="782" y2="83"/><line class="guide-line" x1="766" y1="148" x2="782" y2="148"/>
    <text x="766" y="116" text-anchor="middle" class="dim-label" transform="rotate(-90 766 116)">TEAR</text>
    <text x="793" y="116" text-anchor="middle" class="dim" transform="rotate(-90 793 116)">20.00 mm (0.79 in)</text>

    <line class="guide-line" x1="832" y1="83" x2="832" y2="198"/>
    <line class="guide-line" x1="824" y1="83" x2="840" y2="83"/><line class="guide-line" x1="824" y1="198" x2="840" y2="198"/>
    <text x="822" y="136" text-anchor="middle" class="dim-label" transform="rotate(-90 822 136)">ZIPPER</text>
    <text x="851" y="140" text-anchor="middle" class="dim" transform="rotate(-90 851 140)">35.00 mm (1.38 in)</text>

    <line class="guide-line" x1="769" y1="591" x2="769" y2="697"/>
    <line class="guide-line" x1="761" y1="591" x2="777" y2="591"/><line class="guide-line" x1="761" y1="697" x2="777" y2="697"/>
    <text x="753" y="644" text-anchor="middle" class="dim-label" transform="rotate(-90 753 644)">WINDOW</text>
    <text x="788" y="644" text-anchor="middle" class="dim" transform="rotate(-90 788 644)">32.00 mm (1.26 in)</text>

    <line class="guide-line" x1="759" y1="847" x2="759" y2="1145"/>
    <line class="guide-line" x1="751" y1="847" x2="767" y2="847"/><line class="guide-line" x1="751" y1="996" x2="767" y2="996"/><line class="guide-line" x1="751" y1="1145" x2="767" y2="1145"/>
    <text x="784" y="921" text-anchor="middle" class="dim" transform="rotate(-90 784 921)">45.00 mm (1.77 in)</text>
    <text x="784" y="1070" text-anchor="middle" class="dim" transform="rotate(-90 784 1070)">45.00 mm (1.77 in)</text>
  </g>
</svg>
</body>
</html>
```